Career Counsellor needs vibrant, professional flyer to promote inspiring new webinar

I need a flyer design, A5, double sided. I am a Career Counsellor who helps professionals create fulfilling and inspiring careers and am running a free webinar to promote my program.

I want a design which is simple, elegant and professional with the copy as below. I like dark backgrounds in general (also my name is Wren!!)
I have attached my logo, profile photo and a couple of stock photos to provide an ideal of look/feel (but you can use different stock images if you find something better).

My brand colours are:
Primary - Teal 208FA0
Highlight - Salmon F3745D
with Grey or Wren.

Copy:

(Headline)
Figuring out your next career move is easier than you think...

(webinar details)
FREE WEBINAR
"Why Working Life Can Feel Purposeful Again Using One Simple Weekly Habit Plan"
Weds 3rd Oct 7.30pm (AWST Perth)
Register here: https://zuvrel.link/7kqWzeP

(my profile)
As a Career Counsellor with 14 years of mining industry experience, I’m passionate about helping professionals get inspired by their careers.

(testimonials)
"Ilse is amazing. I am so excited to now have a direction. I have finally found that spark again."
- Corinne Fadley -

"Ilse steered me carefully and faithfully resulting in concrete outcomes with razor sharp clarity for me about how to proceed."
- Margit Ostby -

Target Market(s)

My target audience are mainly professional women, but also men, aged 35-45.

Font styles to use
Sans Serif
Other font styles liked:
• Logo is montserrat extra light

Requirements
Must have
• Copy provided plus profile picture and logo.
• Stylish, creative but simple design.

```html
<!DOCTYPE html>
<html lang="en">
<head>
<meta charset="utf-8">
<title>Free Webinar Flyer – Ilse Wren</title>
<link rel="stylesheet" href="https://fonts.googleapis.com/css2?family=Noto+Sans:wght@400;700&family=Montserrat:wght@200&display=swap">
<style>
  :root {
    --salmon: #f4525f;
    --teal: #2db5a6;
    --ink: #1c1c1c;
    --paper: #ffffff;
    --shadow: rgba(0, 0, 0, 0.55);
  }
  * { margin: 0; padding: 0; box-sizing: border-box; }
  html, body { width: 840px; height: 1200px; overflow: hidden; background: var(--paper); }
  .flyer {
    position: relative;
    width: 840px;
    height: 1200px;
    overflow: hidden;
    background: var(--paper);
    font-family: "Noto Sans", Verdana, sans-serif;
    color: var(--ink);
  }
  .hero-band {
    position: absolute;
    left: 0; top: 0;
    width: 840px; height: 664px;
    background: var(--salmon);
  }
  .section-badge {
    position: absolute;
    left: 262px; top: 53px;
    width: 315px; height: 73px;
    background: var(--teal);
    color: var(--paper);
    font-weight: 700;
    font-size: 40px;
    line-height: 73px;
    text-align: center;
    letter-spacing: 0.5px;
  }
  .badge-rule {
    position: absolute;
    left: 233px; width: 372px; height: 3px;
    background: var(--paper);
  }
  .badge-rule.upper { top: 140px; }
  .badge-rule.lower { top: 149px; }
  .testimonial {
    position: absolute;
    left: 46px; width: 760px;
  }
  .testimonial .quote {
    font-size: 29px;
    line-height: 41px;
    letter-spacing: 0.3px;
  }
  .testimonial .author {
    margin-top: 16px;
    text-align: right;
    font-size: 29px;
    line-height: 41px;
    padding-right: 14px;
  }
  .testimonial.first { top: 192px; }
  .testimonial.second { top: 405px; }
  .webinar-card {
    position: absolute;
    left: 38px; top: 620px;
    width: 764px; height: 556px;
    background: var(--paper);
    border-radius: 18px;
    box-shadow: 0 8px 6px -2px var(--shadow), 0 1px 4px rgba(0,0,0,0.12);
    color: var(--salmon);
    text-align: center;
  }
  .webinar-label {
    position: absolute;
    left: 0; right: 0; top: 25px;
    font-size: 43px;
    line-height: 60px;
    text-decoration: underline;
    text-decoration-thickness: 2px;
    text-underline-offset: 6px;
  }
  .webinar-title {
    position: absolute;
    left: 20px; right: 20px; top: 122px;
    font-size: 34px;
    line-height: 43px;
    letter-spacing: 0.3px;
  }
  .webinar-date {
    position: absolute;
    left: 0; right: 0; top: 290px;
    font-size: 35px;
    line-height: 48px;
    letter-spacing: 0.3px;
  }
  .webinar-register {
    position: absolute;
    left: 0; right: 0; top: 360px;
    font-size: 35px;
    line-height: 48px;
    letter-spacing: 0.3px;
  }
  .brand {
    position: absolute;
    right: 34px; top: 448px;
    display: flex;
    align-items: center;
    gap: 14px;
  }
  .brand-dot {
    width: 40px; height: 40px;
    border-radius: 50%;
    background: var(--teal);
  }
  .brand-name {
    font-family: "Montserrat", sans-serif;
    font-weight: 200;
    font-size: 48px;
    line-height: 60px;
    color: var(--ink);
  }
</style>
</head>
<body>
  <main class="flyer">
    <div class="hero-band"></div>

    <div class="section-badge">Testimonials</div>
    <div class="badge-rule upper"></div>
    <div class="badge-rule lower"></div>

    <blockquote class="testimonial first">
      <p class="quote">"Ilse is amazing. I am so excited to now have a direction. I have finally found that spark again."</p>
      <p class="author">- Corinne Fadley -</p>
    </blockquote>

    <blockquote class="testimonial second">
      <p class="quote">"Ilse steered me carefully and faithfully<br>resulting in concrete outcomes with razor sharp<br>clarity for me about how to proceed."</p>
      <p class="author">- Margit Ostby -</p>
    </blockquote>

    <section class="webinar-card">
      <h2 class="webinar-label">FREE WEBINAR</h2>
      <p class="webinar-title">"Why Working Life Can Feel Purposeful<br>Again Using One Simple Weekly<br>Habit Plan"</p>
      <p class="webinar-date">Weds 3rd Oct 7.30pm (AWST Perth)</p>
      <p class="webinar-register">Register here: https://zuvrel.link/7kqWzeP</p>
      <div class="brand">
        <span class="brand-dot"></span>
        <span class="brand-name">Ilse Wren</span>
      </div>
    </section>
  </main>
</body>
</html>
```